Business Card Design Project

I need some business cards with the logo you did for us (attached)
I am looking for a coulourful yet serious business card

We do market research
on the back I want the logo

on the front my name : Corinne Valdessac
position : Manager
address : Brume Analytica Sarl - 27 Rue des tanneurs
1847 Glarency - Switzerland
corinne.valdessac@brumeanalytica.ch
Tel : +4122 934 07 58
Mob France :+33 671 42 8356
Mob Italy +39 347 520 8163

The tree of the logo could also be used alone

THE BACKGROUND COLOR ON THE FRONT HAS TO BE WHITE, ON THE BACK YU CAN TRY OHER COLOUR BUT HOMOGENEOUS (NOT EXPENSIVE TO PRINT)

Target Market(s)

multinational companies or other market research companies

Industry/Entity Type

Market Research

Requirements
Must have
• logo on the back
and all the info above

```html
<!DOCTYPE html>
<html lang="en">
<head>
<meta charset="utf-8">
<title>Brume Analytica – Business Card</title>
<link rel="stylesheet" href="https://fonts.googleapis.com/css2?family=Arimo:wght@400;700&display=swap">
<style>
  :root {
    --magenta: #d8245f;
    --magenta-soft: #e2578a;
    --crimson: #b01f33;
    --maroon: #6e2630;
    --ink: #3a3a3a;
    --paper: #f7f6f5;
    --stage: #e4e4e4;
  }
  * { box-sizing: border-box; margin: 0; padding: 0; }
  html, body { width: 1200px; height: 880px; overflow: hidden; }
  body {
    background: var(--stage);
    font-family: "Arimo", Arial, sans-serif;
    display: flex;
    align-items: center;
    justify-content: center;
    gap: 60px;
  }
  .card {
    width: 520px;
    height: 336px;
    border-radius: 22px;
    overflow: hidden;
    position: relative;
    box-shadow: 0 6px 18px rgba(0,0,0,0.18);
  }

  /* Back */
  .card-back {
    background: var(--magenta);
    display: flex;
    flex-direction: column;
    align-items: center;
    justify-content: center;
    gap: 14px;
  }
  .brand {
    display: flex;
    align-items: center;
    gap: 12px;
  }
  .brand-dot {
    border-radius: 50%;
    background: var(--maroon);
  }
  .brand-name {
    color: var(--maroon);
    font-weight: 400;
    letter-spacing: -0.5px;
  }
  .card-back .brand-dot { width: 30px; height: 30px; }
  .card-back .brand-name { font-size: 46px; }
  .card-back .site {
    color: var(--magenta-soft);
    filter: brightness(1.15);
    font-size: 15px;
    letter-spacing: 3px;
  }

  /* Front */
  .card-front { background: var(--paper); }
  .card-front .brand {
    position: absolute;
    left: 34px;
    top: 46px;
  }
  .card-front .brand-dot { width: 16px; height: 16px; }
  .card-front .brand-name { font-size: 26px; }

  .holder {
    position: absolute;
    left: 250px;
    top: 110px;
    color: var(--crimson);
    font-size: 17px;
    font-weight: 700;
  }
  .holder .role {
    color: var(--ink);
    font-size: 11px;
    font-weight: 400;
    margin-left: 4px;
  }
  .address-band {
    position: absolute;
    left: 236px;
    right: 0;
    top: 134px;
    height: 38px;
    background: var(--crimson);
    color: #fff;
    font-size: 10.5px;
    line-height: 14px;
    padding: 5px 0 0 14px;
  }
  .contacts {
    position: absolute;
    left: 250px;
    top: 180px;
    list-style: none;
    font-size: 11px;
    line-height: 15px;
    color: var(--ink);
  }
  .contacts .label {
    color: var(--magenta);
    font-size: 9px;
    display: inline-block;
    width: 62px;
  }
  .site-band {
    position: absolute;
    left: 0;
    right: 0;
    top: 252px;
    height: 52px;
    background: var(--magenta);
    color: #fff;
    font-size: 19px;
    letter-spacing: 4px;
    display: flex;
    align-items: center;
    padding-left: 40px;
  }
</style>
</head>
<body>
  <section class="card card-back" aria-label="Card back">
    <div class="brand">
      <span class="brand-dot"></span>
      <span class="brand-name">brume analytica</span>
    </div>
    <p class="site">www.brumeanalytica.ch</p>
  </section>

  <section class="card card-front" aria-label="Card front">
    <div class="brand">
      <span class="brand-dot"></span>
      <span class="brand-name">brume analytica</span>
    </div>
    <p class="holder">Corinne Valdessac<span class="role">Manager</span></p>
    <div class="address-band">
      Brume Analytica Sarl - 27 Rue des tanneurs<br>
      1847 Glarency - Switzerland
    </div>
    <ul class="contacts">
      <li><span class="label">tel</span>+4122 934 07 58</li>
      <li><span class="label">mob france</span>+33 671 42 8356</li>
      <li><span class="label">mob italy</span>+39 347 520 8163</li>
      <li><span class="label">email</span>corinne.valdessac@brumeanalytica.ch</li>
    </ul>
    <div class="site-band">www.brumeanalytica.ch</div>
  </section>
</body>
</html>
```